Stationery for tax services company
Ledger Harbor Advisors
Stationery for tax services company - Financial Services
Creative Brief
Simple
Colin T. Westbrook, EA, JD, MST
President
4817 North Palomar Avenue, Suite 6 Honolulu, HI 96814
fileclearhelp@mailvora.net
www.LedgerHarborAdvisors.net
I also need business cards for the 2 following people: [Beth Colton, EA / Tax Preparer] [Marla Penhurst / Executive Assistant]
We need a design for business cards, letterhead page 1 of 2, letterhead page 2 of 2, envelopes small, label for large envelopes, fax cover sheet, email signature, and presentation folders.

```html
<!DOCTYPE html>
<html lang="en">
<head>
<meta charset="utf-8">
<title>Ledger Harbor Advisors — Stationery</title>
<link rel="stylesheet" href="https://fonts.googleapis.com/css2?family=Cinzel:wght@600&family=Open+Sans:wght@400;600&display=swap">
<style>
  :root {
    --navy: #1f2673;
    --royal: #3a46a8;
    --band-light: #6b74c4;
    --paper: #ffffff;
    --paper-shade: #f3f4f7;
    --grey-env: #9fa2ab;
    --grey-env-dark: #7d808a;
    --ink: #4b4f5c;
    --ink-soft: #9a9eaa;
    --stage: #e9e6e2;
    --label: #8a857f;
    --faint: #dfe2ee;
  }
  * { box-sizing: border-box; margin: 0; padding: 0; }
  html, body { width: 1200px; height: 466px; overflow: hidden; }
  body { background: var(--stage); position: relative; font-family: "Open Sans", sans-serif; color: var(--ink); }

  .piece { position: absolute; box-shadow: 0 2px 6px rgba(0,0,0,.18); overflow: hidden; }
  .caption { position: absolute; font-size: 6px; letter-spacing: 1.2px; text-transform: uppercase; color: var(--label); text-align: center; }

  .brand { font-family: "Cinzel", serif; font-weight: 600; color: var(--navy); display: flex; align-items: center; gap: 4px; line-height: 1.05; }
  .brand-mark { width: 7px; height: 7px; background: var(--navy); flex: none; }

  /* Business cards */
  .card { width: 115px; height: 62px; left: 24px; }
  .card-front { top: 190px; background: var(--paper); padding: 10px 8px; }
  .card-front .brand { font-size: 6px; }
  .card-front .card-person { margin-top: 8px; font-size: 4px; color: var(--ink); line-height: 1.5; }
  .card-front .card-band { position: absolute; left: 0; right: 0; bottom: 0; height: 5px; background: linear-gradient(90deg, var(--navy), var(--band-light)); }
  .card-back { top: 281px; background: linear-gradient(135deg, var(--navy), var(--royal)); display: flex; align-items: center; justify-content: center; }
  .card-back .brand { color: var(--paper); font-size: 7px; }
  .card-back .brand-mark { background: var(--paper); }

  /* Letterheads */
  .letterhead { top: 36px; width: 350px; height: 408px; background: var(--paper); }
  .letterhead-one { left: 163px; }
  .letterhead-two { left: 540px; }
  .letterhead .brand { position: absolute; left: 24px; top: 22px; font-size: 10px; width: 150px; }
  .letterhead .brand-mark { width: 10px; height: 10px; }
  .header-contact { position: absolute; left: 190px; top: 20px; font-size: 4.5px; line-height: 1.7; color: var(--ink); }
  .faint-name { position: absolute; left: 0; right: 0; top: 165px; text-align: center; font-family: "Cinzel", serif; font-weight: 600; font-size: 30px; color: var(--faint); line-height: 1.1; }
  .footer-band { position: absolute; left: 0; right: 0; bottom: 38px; height: 12px; background: linear-gradient(90deg, var(--navy), var(--royal) 60%, var(--band-light)); }
  .footer-band::after { content: ""; position: absolute; left: 0; right: 0; top: 4px; height: 1px; background: rgba(255,255,255,.55); }
  .footer-text { position: absolute; left: 0; right: 0; bottom: 22px; text-align: center; font-size: 4.5px; color: var(--ink-soft); letter-spacing: .4px; }

  /* Envelopes */
  .envelope { left: 924px; width: 252px; height: 84px; }
  .env-blue { top: 36px; background: var(--navy); }
  .env-grey { top: 148px; background: var(--grey-env); }
  .env-white { top: 240px; background: var(--paper-shade); }
  .envelope svg { position: absolute; inset: 0; }
  .envelope .brand { position: absolute; font-size: 5px; }
  .env-blue .brand { left: 110px; top: 44px; color: var(--paper); }
  .env-blue .brand-mark { background: var(--paper); }
  .env-grey .brand { left: 110px; top: 48px; }
  .env-white .brand { left: 110px; top: 48px; }
  .env-front { top: 336px; left: 924px; width: 252px; height: 108px; background: var(--paper); }
  .env-front .brand { position: absolute; left: 14px; top: 14px; font-size: 7px; }
  .env-front .return { position: absolute; left: 14px; top: 30px; font-size: 4px; color: var(--ink); line-height: 1.6; }
  .env-front .env-band { position: absolute; left: 0; right: 0; bottom: 14px; height: 9px; background: linear-gradient(90deg, var(--navy), var(--royal) 60%, var(--band-light)); }
  .env-front .env-foot { position: absolute; left: 0; right: 0; bottom: 4px; text-align: center; font-size: 4px; color: var(--ink-soft); }
</style>
</head>
<body>

  <div class="caption" style="left:24px; top:170px; width:115px;">Stationery Concepts</div>

  <section class="piece card card-front" aria-label="Business card front">
    <div class="brand"><span class="brand-mark"></span>Ledger Harbor Advisors</div>
    <div class="card-person">Colin T. Westbrook, EA, JD, MST<br>President<br>fileclearhelp@mailvora.net</div>
    <div class="card-band"></div>
  </section>
  <div class="caption" style="left:24px; top:258px; width:115px;">Business Card Front</div>

  <section class="piece card card-back" aria-label="Business card back">
    <div class="brand"><span class="brand-mark"></span>Ledger Harbor Advisors</div>
  </section>
  <div class="caption" style="left:24px; top:349px; width:115px;">Business Card Back</div>

  <section class="piece letterhead letterhead-one" aria-label="Letterhead page 1">
    <div class="brand"><span class="brand-mark"></span>Ledger Harbor Advisors</div>
    <div class="header-contact">
      Colin T. Westbrook, EA, JD, MST<br>
      4817 North Palomar Avenue, Suite 6<br>
      Honolulu, HI 96814<br>
      Phone: (808) 555-0142<br>
      Fax: (808) 555-0198
    </div>
    <div class="faint-name">Ledger Harbor<br>Advisors</div>
    <div class="footer-band"></div>
    <div class="footer-text">fileclearhelp@mailvora.net &nbsp;|&nbsp; www.LedgerHarborAdvisors.net</div>
  </section>
  <div class="caption" style="left:163px; top:452px; width:350px;">Letterhead Page 1</div>

  <section class="piece letterhead letterhead-two" aria-label="Letterhead page 2">
    <div class="brand"><span class="brand-mark"></span>Ledger Harbor Advisors</div>
    <div class="faint-name">Ledger Harbor<br>Advisors</div>
    <div class="footer-band"></div>
    <div class="footer-text">4817 North Palomar Avenue, Suite 6 &nbsp;|&nbsp; Honolulu, HI 96814</div>
  </section>
  <div class="caption" style="left:540px; top:452px; width:350px;">Letterhead Page 2</div>

  <section class="piece envelope env-blue" aria-label="Envelope back, blue">
    <svg width="252" height="84" viewBox="0 0 252 84"><polygon points="0,0 252,0 126,38" fill="#2c3590"/><polyline points="0,0 126,38 252,0" fill="none" stroke="#151b56" stroke-width="1"/></svg>
    <div class="brand"><span class="brand-mark"></span>Ledger Harbor Advisors</div>
  </section>

  <section class="piece envelope env-grey" aria-label="Envelope back, grey">
    <svg width="252" height="84" viewBox="0 0 252 84"><polygon points="0,0 252,0 238,34 14,34" fill="var(--grey-env-dark)"/></svg>
    <div class="brand"><span class="brand-mark"></span>Ledger Harbor Advisors</div>
  </section>

  <section class="piece envelope env-white" aria-label="Envelope back, white">
    <svg width="252" height="84" viewBox="0 0 252 84"><polygon points="0,0 252,0 238,34 14,34" fill="#ffffff" stroke="#d8dae0" stroke-width="1"/></svg>
    <div class="brand"><span class="brand-mark"></span>Ledger Harbor Advisors</div>
  </section>

  <section class="piece env-front" aria-label="Envelope front">
    <div class="brand"><span class="brand-mark"></span>Ledger Harbor Advisors</div>
    <div class="return">4817 North Palomar Avenue, Suite 6<br>Honolulu, HI 96814</div>
    <div class="env-band"></div>
    <div class="env-foot">www.LedgerHarborAdvisors.net</div>
  </section>
  <div class="caption" style="left:924px; top:452px; width:252px;">Envelope</div>

</body>
</html>
```